Wordpress Design for a Business Blog

We are running the finance blog kivo.net and want to renew our web page design. Thus, we need a new designed Wordpress theme containing an overview page, used on the front page and the start pages of the categories, and a single article view like on http://kivo.net/blog/coping-with-falling-dollar/ . The new look should be serious, should contain all elements of the current website, should look professional (no entertainment elements) and in light colors.
Updates

Reason: Due to some request, we've extended the deadline a few days.

Reason: Hello,

we received a comment that our budget is to low for  a complete Wordpress design including coding. Thus, we changed our requriement to psd design  only,  without coding.

Industry/Entity Type

Entertainment

Requirements
Must have
• * Light colors
* Two column layout
* Contain all elements of the current website www.kivo.net
Should not have
• * Too much colors
* Look to flashy

```html
<!DOCTYPE html>
<html lang="en">
<head>
<meta charset="utf-8">
<title>kivo.net – Finance Blog</title>
<link rel="stylesheet" href="https://fonts.googleapis.com/css2?family=Arimo:wght@400;700&family=Roboto+Condensed:wght@700&family=Gelasio:wght@400;700&display=swap">
<style>
:root{
  --green:#6cb31c;
  --green-light:#9fd44a;
  --green-dark:#3c8a0c;
  --nav-top:#d6efb0;
  --nav-bottom:#8cc43c;
  --blue:#3a92d6;
  --blue-dark:#1c6aa8;
  --navy:#0c3263;
  --link:#1b7fc6;
  --text:#333333;
  --muted:#666666;
  --page:#e4e9ee;
  --panel-border:#c9d2da;
  --welcome-bg:#f7f4ef;
  --orange:#f07a12;
  --ad-bg:#e3e7eb;
  --white:#ffffff;
}
*{box-sizing:border-box;margin:0;padding:0}
html,body{width:1200px;height:2285px;overflow:hidden}
body{position:relative;background:var(--page);font-family:"Arimo",Arial,sans-serif;color:var(--text)}
a{color:inherit;text-decoration:none}

/* ===== Header ===== */
.site-header{position:absolute;left:0;top:0;width:1200px;height:191px;
  background:linear-gradient(180deg,var(--green-light) 0%,var(--green) 55%,var(--green-dark) 100%);overflow:hidden}
.site-header .sheen{position:absolute;left:0;top:0}
.utility-bar{position:absolute;left:707px;top:0;width:493px;height:39px;background:linear-gradient(180deg,#4aa2e2,#2474b8);
  border-bottom-left-radius:16px;display:flex;align-items:center;padding-left:24px;gap:22px;color:var(--white);font-size:16px}
.search-field{position:absolute;left:178px;top:7px;width:283px;height:26px;background:var(--white);border-radius:3px;
  font-size:12px;color:#999;padding:6px 8px}
.search-field svg{position:absolute;right:8px;top:4px}
.brand{position:absolute;left:26px;top:80px;font-family:"Arimo",Arial,sans-serif;font-weight:700;font-size:48px;color:var(--white);line-height:1}
.tagline{position:absolute;left:348px;top:92px;font-family:"Roboto Condensed",Arial,sans-serif;font-weight:700;font-size:30px;
  color:var(--white);text-transform:uppercase;letter-spacing:.2px;line-height:1}

/* ===== Navigation ===== */
.main-nav{position:absolute;left:0;top:191px;width:1200px;height:55px;background:linear-gradient(180deg,var(--nav-top),var(--nav-bottom));
  border-bottom:1px solid #6aa227}
.main-nav a{position:absolute;top:17px;font-size:19px;color:#253a0c}
.main-nav a.current{left:13px;top:8px;width:87px;height:40px;background:linear-gradient(180deg,#ffffff,#e8e8e8);border-radius:5px;
  border:1px solid #9aaa88;text-align:center;padding-top:8px}
.feed-button{position:absolute;left:1117px;top:191px;width:66px;height:60px;background:linear-gradient(180deg,#ff9b3a,var(--orange));
  border-radius:6px;border:2px solid #c05e08}

/* ===== Welcome band ===== */
.welcome-band{position:absolute;left:0;top:246px;width:1200px;height:384px;background:linear-gradient(180deg,#5aaee8,var(--blue) 60%,#2d82c6)}
.welcome-box{position:absolute;left:13px;top:19px;width:861px;height:348px;background:var(--welcome-bg);border:2px solid #d8e6f2;border-radius:3px}
.welcome-title{position:absolute;left:26px;top:30px;font-family:"Arimo",Arial,sans-serif;font-size:30px;color:#222}
.welcome-title span{color:var(--green);font-weight:700}
.welcome-rule{position:absolute;left:26px;top:64px;width:651px;border-top:2px dotted #555}
.welcome-text{position:absolute;left:26px;top:81px;width:651px;font-size:12.5px;line-height:21px;text-align:justify;color:#333}
.welcome-text p+p{margin-top:15px}
.read-more{position:absolute;left:22px;top:306px;width:161px;height:30px;background:linear-gradient(180deg,#4c9ee0,#1f68ad);
  color:var(--white);font-size:15px;padding:6px 0 0 14px;border-radius:2px}
.read-more svg{position:absolute;right:10px;top:10px}
.welcome-photo{position:absolute;left:698px;top:17px;width:154px;height:311px;padding:4px;background:var(--white);border:1px solid #bcd}
.welcome-photo div{width:100%;height:100%;background:linear-gradient(160deg,#f2f4f2 0%,#a9c49a 45%,#6f8f6a 70%,#e9ece8 100%)}

/* ===== Posts column ===== */
.posts-panel{position:absolute;left:15px;top:643px;width:859px;height:1527px;background:var(--white);border:1px solid var(--panel-border)}
.post{position:absolute;left:13px;width:835px;height:280px}
.post-title{position:absolute;left:0;top:0;font-size:21px;color:var(--link);font-weight:400}
.post-meta{position:absolute;left:0;top:36px;font-size:12px;color:#222;white-space:nowrap}
.post-meta b{font-weight:700}
.post-meta a{color:var(--link)}
.post-rule{position:absolute;left:0;top:56px;width:835px;border-top:2px dotted #777}
.post-excerpt{position:absolute;left:0;top:64px;width:548px;font-size:12.8px;line-height:23px;color:#333}
.post-excerpt p+p{margin-top:22px}
.post-thumb{position:absolute;left:561px;top:65px;width:270px;height:178px;border:1px solid #bbb;padding:3px;background:var(--white)}
.post-thumb div{width:100%;height:100%}
.share-row{position:absolute;left:569px;top:250px;display:flex;gap:9px}
.share-row span{width:24px;height:24px;border-radius:3px;display:block}
.posts-rule{position:absolute;left:13px;top:1460px;width:835px;border-top:2px dotted #777}
.more-posts{position:absolute;left:676px;top:1477px;width:174px;height:43px;background:linear-gradient(180deg,#7cc43a,#3c8a0c);
  border-radius:3px;color:var(--white);font-weight:700;font-size:17px;text-align:center;padding-top:12px}

/* ===== Sidebar ===== */
.widget{position:absolute;left:885px;width:293px;border-radius:6px;border:2px solid #cfe0ee;color:var(--white)}
.widget.green{background:linear-gradient(180deg,#8cc83e,#4f9a16)}
.widget.blue{background:linear-gradient(180deg,#3e96d8,#1d67a4)}
.widget h3{font-family:"Gelasio",Georgia,serif;font-weight:400;font-size:28px;position:absolute;left:13px;top:6px}
.widget ul{list-style:none;position:absolute;left:18px;font-size:11.5px}
.widget li{height:23px;line-height:23px;white-space:nowrap}
.widget li::before{content:"» ";font-weight:700}
.field{position:absolute;height:24px;background:var(--white);border:1px solid #aab;font-size:11px;color:#777;padding:4px 6px}
.go-button{position:absolute;left:13px;top:72px;width:57px;height:29px;background:linear-gradient(180deg,#4aa2e2,#1f68ad);
  border-radius:3px;font-size:14px;font-weight:700;text-align:center;padding-top:5px}
.select-field{position:absolute;left:15px;top:44px;width:246px;height:24px;background:var(--white);font-size:11px;color:#555;padding:5px 6px}
.select-field span{position:absolute;right:3px;top:3px;width:17px;height:17px;background:#222}
.advert{position:absolute;left:885px;width:293px;background:var(--ad-bg);border:2px solid #b9c3cc;border-radius:6px;
  font-family:"Gelasio",Georgia,serif;font-size:28px;color:#111;display:flex;align-items:center;justify-content:center}
.tag-cloud{position:absolute;left:15px;top:66px;width:262px;line-height:29px}
.tag-cloud a{margin-right:4px;white-space:nowrap}

/* ===== Footer ===== */
.site-footer{position:absolute;left:0;top:2187px;width:1200px;height:98px;background:var(--navy);border-top:4px solid #2a5a90;
  color:#dfe8f2;font-size:12.5px;text-align:center}
.footer-links{position:absolute;left:0;top:30px;width:100%}
.copyright{position:absolute;left:0;top:51px;width:100%}
</style>
</head>
<body>

<header class="site-header">
  <svg class="sheen" width="1200" height="191" viewBox="0 0 1200 191" aria-hidden="true">
    <polygon points="560,191 760,0 1000,0 820,191" fill="#ffffff" opacity="0.08"/>
    <polygon points="860,191 1050,0 1200,0 1200,191" fill="#ffffff" opacity="0.06"/>
    <polygon points="0,191 0,120 300,191" fill="#000000" opacity="0.05"/>
  </svg>
  <nav class="utility-bar">
    <a href="#">About</a>
    <a href="#">Tag Cloud</a>
    <div class="search-field">Type your search here
      <svg width="18" height="18" viewBox="0 0 18 18"><circle cx="7" cy="7" r="5" fill="none" stroke="#222" stroke-width="2"/><line x1="11" y1="11" x2="16" y2="16" stroke="#222" stroke-width="3"/></svg>
    </div>
  </nav>
  <div class="brand">kivo.net</div>
  <div class="tagline">kivo.net is all about achieving your financial goals</div>
</header>

<nav class="main-nav">
  <a class="current" href="#">Home</a>
  <a href="#" style="left:122px">Finance</a>
  <a href="#" style="left:226px">Economy</a>
  <a href="#" style="left:348px">Resources</a>
  <a href="#" style="left:474px">Personal Saving</a>
  <a href="#" style="left:648px">Make Money</a>
  <a href="#" style="left:809px">Miscellanious</a>
  <a href="#" style="left:948px">Uncategorized</a>
</nav>
<a class="feed-button" href="#" aria-label="Subscribe to feed"></a>

<section class="welcome-band">
  <div class="welcome-box">
    <h1 class="welcome-title">welcome to <span>KIVO.NET</span></h1>
    <div class="welcome-rule"></div>
    <div class="welcome-text">
      <p>Lorem ipsum dolor sit amet, consectetur adipiscing elit. Sed sit amet sem sit amet urna tincidunt suscipit. Donec vel leo ac erat sodales egestas rhoncus a sem. In non elit lorem, non congue magna. Donec facilisis augue ut nisl venenatis quis aliquet felis accumsan. Nulla urna neque, consequat non semper ut, viverra sed enim. Etiam placerat, dolor eget iaculis sollicitudin, lorem eros ornare nibh, in iaculis est lorem vitae ipsum.</p>
      <p>Integer eu porta magna. In vulputate ultricies nisl vel convallis. Cras scelerisque elementum arcu non laoreet. Etiam justo lacus, tincidunt eget tincidunt eu, dignissim ac orci. Phasellus in purus ante. Nam porta enim sit amet sem molestie in rutrum augue fermentum. Donec feugiat volutpat mauris nec congue. Praesent blandit sagittis lectus eget scelerisque.</p>
    </div>
    <a class="read-more" href="#">Read More
      <svg width="26" height="10" viewBox="0 0 26 10"><path d="M2 1l4 4-4 4M9 1l4 4-4 4M16 1l4 4-4 4" fill="none" stroke="#fff" stroke-width="2"/></svg>
    </a>
    <div class="welcome-photo"><div role="img" aria-label="Photo of a small house folded from banknotes"></div></div>
  </div>
</section>

<main class="posts-panel">
  <article class="post" style="top:16px">
    <h2 class="post-title">Money/ Saving Jokes</h2>
    <div class="post-meta"><b>Posted by Dana</b> in <a href="#">Economy,Finance,Miscellaneous,Personal Saving,Resources,Uncategorized</a> <b>on June 1, 2011 &nbsp;| no responses</b></div>
    <div class="post-rule"></div>
    <div class="post-excerpt">
      <p>Here are some jokes about money/ saving I found online. I hope you'll have fun reading them. Enjoy! My mother decided to trim her household budget wherever possible, so instead of having a dress dry-cleaned she washed it by hand. Proud of her savings, she boasted to my father, "Just think, Fred, we are five [...]</p>
      <p>Here are some jokes about money/ saving I found online. I hope you'll have fun reading them. Enjoy! My mother decided to trim her household budget wherever possible, so instead of having a dress dry-cleaned she washed it by hand. Proud of her savings, she boasted to my father, "Just think, Fred, we are five [...]</p>
    </div>
    <div class="post-thumb"><div role="img" aria-label="Black and white cartoon about household savings" style="background:linear-gradient(135deg,#f4f4f4,#c9c9c9)"></div></div>
    <div class="share-row"><span style="background:#3b5b99"></span><span style="background:#7cc62b"></span><span style="background:#8a97a8"></span><span style="background:#3b74b8"></span><span style="background:#2c8fc1"></span><span style="background:#3aa34a"></span><span style="background:#2d4fa0"></span><span style="background:#4cae2c"></span></div>
  </article>

  <article class="post" style="top:307px">
    <h2 class="post-title">Money/ Saving Jokes</h2>
    <div class="post-meta"><b>Posted by Dana</b> in <a href="#">Economy,Finance,Miscellaneous,Personal Saving,Resources,Uncategorized</a> <b>on June 1, 2011 &nbsp;| no responses</b></div>
    <div class="post-rule"></div>
    <div class="post-excerpt">
      <p>Here are some jokes about money/ saving I found online. I hope you'll have fun reading them. Enjoy! My mother decided to trim her household budget wherever possible, so instead of having a dress dry-cleaned she washed it by hand. Proud of her savings, she boasted to my father, "Just think, Fred, we are five [...]</p>
      <p>Here are some jokes about money/ saving I found online. I hope you'll have fun reading them. Enjoy! My mother decided to trim her household budget wherever possible, so instead of having a dress dry-cleaned she washed it by hand. Proud of her savings, she boasted to my father, "Just think, Fred, we are five [...]</p>
    </div>
    <div class="post-thumb"><div role="img" aria-label="Photo of a euro sign chained to a ball" style="background:radial-gradient(circle at 50% 55%,#7d7d7d,#d8d8d8 45%,#fafafa 75%)"></div></div>
    <div class="share-row"><span style="background:#3b5b99"></span><span style="background:#7cc62b"></span><span style="background:#8a97a8"></span><span style="background:#3b74b8"></span><span style="background:#2c8fc1"></span><span style="background:#3aa34a"></span><span style="background:#2d4fa0"></span><span style="background:#4cae2c"></span></div>
  </article>

  <article class="post" style="top:601px">
    <h2 class="post-title">Surviving the Euro Crisis</h2>
    <div class="post-meta"><b>Posted by Theo</b> in <a href="#">Economy,Finance,Miscellaneous,Personal Saving,Resources,Uncategorized</a> <b>on May 20, 2011 &nbsp;| no responses</b></div>
    <div class="post-rule"></div>
    <div class="post-excerpt">
      <p>Aside from the falling dollar, the global economy today is also struggling with the Euro crisis. To prevent a second financial crisis, definite and strict measures must be taken to stabilize not only Europe but the worldwide economy as a whole. Germany is trying to solve this dilemma by regulating the markets and pacifying the .</p>
      <p>Aside from the falling dollar, the global economy today is also struggling with the Euro crisis. To prevent a second financial crisis, definite and strict measures must be taken to stabilize not only Europe but the worldwide economy as a whole. Germany is trying to solve this dilemma by regulating the markets and pacifying the</p>
    </div>
    <div class="post-thumb"><div role="img" aria-label="Ink illustration of a crumpled banknote" style="background:linear-gradient(135deg,#efefef,#a9a9a9 50%,#e6e6e6)"></div></div>
    <div class="share-row"><span style="background:#3b5b99"></span><span style="background:#7cc62b"></span><span style="background:#8a97a8"></span><span style="background:#3b74b8"></span><span style="background:#2c8fc1"></span><span style="background:#3aa34a"></span><span style="background:#2d4fa0"></span><span style="background:#4cae2c"></span></div>
  </article>

  <article class="post" style="top:892px">
    <h2 class="post-title">6 Secrets to Successful Saving</h2>
    <div class="post-meta"><b>Posted by Dana</b> in <a href="#">Economy,Finance,Miscellaneous,Personal Saving,Resources,Uncategorized</a> <b>on April 29, 2011 &nbsp;| no responses</b></div>
    <div class="post-rule"></div>
    <div class="post-excerpt">
      <p>Like they say, you are never too young nor too old to start saving. Especially in today's hard times, we should always be ready for emergencies and other unexpected expenses. So here are six secrets that might just help you to finally succeed in your savings plan. Secret #1: A Realistic, Achievable Savings Goal. Realistic, [...]</p>
      <p>Like they say, you are never too young nor too old to start saving. Especially in today's hard times, we should always be ready for emergencies and other unexpected expenses. So here are six secrets that might just help you to finally succeed in your savings plan. Secret #1: A Realistic, Achievable Savings Goal. Realistic, [...]</p>
    </div>
    <div class="post-thumb"><div role="img" aria-label="Photo of a keyboard key labelled save beside coins" style="background:linear-gradient(160deg,#fafafa,#dcdcdc 55%,#b9a88a 80%,#f2f2f2)"></div></div>
    <div class="share-row"><span style="background:#3b5b99"></span><span style="background:#7cc62b"></span><span style="background:#8a97a8"></span><span style="background:#3b74b8"></span><span style="background:#2c8fc1"></span><span style="background:#3aa34a"></span><span style="background:#2d4fa0"></span><span style="background:#4cae2c"></span></div>
  </article>

  <article class="post" style="top:1166px">
    <h2 class="post-title">6 Secrets to Successful Saving</h2>
    <div class="post-meta"><b>Posted by Dana</b> in <a href="#">Economy,Finance,Miscellaneous,Personal Saving,Resources,Uncategorized</a> <b>on April 29, 2011 &nbsp;| no responses</b></div>
    <div class="post-rule"></div>
    <div class="post-excerpt">
      <p>Like they say, you are never too young nor too old to start saving. Especially in today's hard times, we should always be ready for emergencies and other unexpected expenses. So here are six secrets that might just help you to finally succeed in your savings plan. Secret #1: A Realistic, Achievable Savings Goal. Realistic, [...]</p>
      <p>Like they say, you are never too young nor too old to start saving. Especially in today's hard times, we should always be ready for emergencies and other unexpected expenses. So here are six secrets that might just help you to finally succeed in your savings plan. Secret #1: A Realistic, Achievable Savings Goal. Realistic, [...]</p>
    </div>
    <div class="post-thumb"><div role="img" aria-label="Photo of a keyboard key labelled save beside coins" style="background:linear-gradient(160deg,#fafafa,#dcdcdc 55%,#b9a88a 80%,#f2f2f2)"></div></div>
    <div class="share-row"><span style="background:#3b5b99"></span><span style="background:#7cc62b"></span><span style="background:#8a97a8"></span><span style="background:#3b74b8"></span><span style="background:#2c8fc1"></span><span style="background:#3aa34a"></span><span style="background:#2d4fa0"></span><span style="background:#4cae2c"></span></div>
  </article>

  <div class="posts-rule"></div>
  <a class="more-posts" href="#">Read More Posts</a>
</main>

<aside>
  <section class="widget green" style="top:643px;height:109px">
    <h3>Sign In</h3>
    <div class="field" style="left:13px;top:40px;width:122px">Username</div>
    <div class="field" style="left:143px;top:40px;width:118px">••••••••</div>
    <a class="go-button" href="#">Go</a>
  </section>

  <section class="widget blue" style="top:765px;height:96px">
    <h3>Archives</h3>
    <div class="select-field">Select Month<span></span></div>
  </section>

  <section class="widget blue" style="top:876px;height:202px">
    <h3>Popular Posts</h3>
    <ul style="top:52px">
      <li>Will You Inherit Your Parents' Debt?</li>
      <li>Money Saving Quotes</li>
      <li style="height:auto;line-height:15px;white-space:normal;width:240px;padding:4px 0">Product Labels: More Than Meets The Eye</li>
      <li>Money Saving Quotes</li>
      <li>Product Labels: More Than Meets The</li>
    </ul>
  </section>

  <div class="advert" style="top:1091px;height:205px">Advertisement</div>

  <section class="widget blue" style="top:1309px;height:256px">
    <h3>Categories</h3>
    <ul style="top:52px">
      <li>Finance (38)</li>
      <li>Economy (31)</li>
      <li>Resources (44)</li>
      <li>Personal Saving (45)</li>
      <li>Make Money (13)</li>
      <li>Miscellanious (53)</li>
      <li>Uncategorized (11)</li>
    </ul>
  </section>

  <div class="advert" style="top:1580px;height:198px">Advertisement</div>

  <section class="widget green" style="top:1789px;height:265px">
    <h3>Tags</h3>
    <div class="tag-cloud">
      <a href="#" style="font-size:14px">financial planner</a>
      <a href="#" style="font-size:18px">financial planning</a>
      <a href="#" style="font-size:15px">process</a>
      <a href="#" style="font-size:20px">frugal lifestyle</a>
      <a href="#" style="font-size:14px">frugal living</a>
      <a href="#" style="font-size:20px">overspending</a>
      <a href="#" style="font-size:14px">personal savings</a>
      <a href="#" style="font-size:14px">retirement</a>
      <a href="#" style="font-size:18px">save money</a>
      <a href="#" style="font-size:20px">unemployment</a>
      <a href="#" style="font-size:14px">More Tags</a>
    </div>
  </section>

  <section class="widget blue" style="top:2067px;height:105px">
    <h3>Blogroll</h3>
    <ul style="top:56px"><li>Fundlane.com</li></ul>
  </section>
</aside>

<footer class="site-footer">
  <div class="footer-links">Terms &amp; Conditions &nbsp;|&nbsp; FAQs &nbsp;|&nbsp; Contact Us &nbsp;|&nbsp; About Us</div>
  <div class="copyright">©2011 Copyright kivo.net &nbsp; | &nbsp;All Rights Reserved</div>
</footer>

</body>
</html>
```